電子書籍の表紙デザインをお願い致します。

本の内容、
冴えない20代のOLでした。そんな私でしたが約7年前に、
「たった一度きりのこの人生。もっと自分らしく、もっと輝かせたい。」
と強く熱望した瞬間があり、私は知識・人脈・実績・経験・貯金などビジネスに関してプラスになるような持ち合わせが一切ないゼロの状態で、【私らしい生き方と働き方】を一心に求めて「起業」を目指しはじめました。
今では独立を果たし、当時は未知の世界でしかなかった独立起業の道も今年で7年目に突入しました。得意な分野は、ビジネスコンサルティング、ビジネスプロデュース、コミュニティ運営、Webマーケティング、Webライティング、アフィリエイト、プロモーション、マインドコーチング、オウンドメディア構築など。写真や動画の編集・加工などクリエイティブなことも割と好きです。

私の仕事における共通点はどのビジネスでもパソコン1台とネット環境があれば場所を問わずどこでも仕事ができることです。そのライフスタイルを「スカイハーベスター」と名付け、よく国内外問わず、大好きな旅をしながら仕事をしています。

しかし、この 「起業」という働き方に出会う前の私は、好きなことをしながら仕事ができる、そんなワークスタイルがあるだなんて夢にも思っていませんでした。
そんなの理想のまた理想・・・そんなかんじで。しかしそれ以上に私が伝えたいのは、「自分でビジネスをして価値提供をする」という中で自分の思考や価値観、ライフスタイルまでも大きく変化したということなのです。そして今は毎日に充実感があり、やりがいを感じながら仕事も楽しくしています。

そして現在は、自らの経験と海外で得た感動をもとにPC1台で好きな時に・好きな場所で・好きな人と、「自分らしく、グローバルに生きていく」そんなスタイルを日々全力で、熱狂してご提供しています。

優しい雰囲気の安心できるような女性らしいカラーでお願い致します。

使って頂きたい画像と本文を添付致します。
表紙はこの4枚の画像を使って優しいイメージで、パステルカラー、薄い色を使っていただけると嬉しいです。

タイトルは
きみの毎日は花になる!扉をそっと叩いて
心ほどける日々を選び取るための小さな習慣集
でお願い致します。

はじめに、私の起業ストーリーを少しお話しさせてください。私はもともと自分に自信がまったく持てなくて、そのくせ社会不適合で、ただただ路頭に迷う、冴えない20代のOLでした。そんな私でしたが約7年前に、

日にちを19日まで延長させていただきました。
20日まで延長致しました。宜しくお願い致します。
いま、
最終段階で決定に向けて進めております。
21日で締め切らせていただきます。最後までよろしくお願いいたします。

お洒落な大人女子のイメージややんわりとしたパステルカラーの色合いがとても美しい作品だと感じました。タイトルや入れたい文字をしっかりと目立たせていただきました。自分の思い描くイメージをカタチにしてくださったなと感謝の想いでいっぱいでございます。

この度、ご提案してくださったデザイナーの皆様、最後まで吟味させて頂き、選ぶのにとても迷いました。それほど、素晴らしい作品ばかりでした。沢山のご提案を本当に有難うございました。今回はご縁を頂けなかった皆様とも、今後も定期的にコンペをさせていただく予定ですので、どうぞよろしくお願いします。

```html
<!DOCTYPE html>
<html lang="ja">
<head>
<meta charset="utf-8">
<title>心ほどける日々を選び取るための小さな習慣集</title>
<link rel="stylesheet" href="https://fonts.googleapis.com/css2?family=Noto+Sans+JP:wght@500;700;900&family=Klee+One:wght@600&family=Playfair+Display:ital@0;1&display=swap">
<style>
  :root {
    --blush: #fbe6ef;
    --lilac: #f3e4f6;
    --pink: #ee5f9e;
    --pink-deep: #d9448a;
    --magenta: #e2478f;
    --sky: #2f9fd8;
    --ink: #4a4f63;
    --muted: #8d7c90;
    --white: #ffffff;
  }
  * { margin: 0; padding: 0; box-sizing: border-box; }
  html, body { width: 751px; height: 1200px; overflow: hidden; background: var(--white); }
  .cover {
    position: relative;
    width: 751px; height: 1200px;
    overflow: hidden;
    font-family: "Noto Sans JP", sans-serif;
    background: linear-gradient(180deg, var(--lilac) 0%, var(--blush) 20%, #fff4f8 40%, #ffffff 100%);
  }
  .cover p, .cover span { white-space: nowrap; }
  .tagline-en {
    position: absolute; top: 8px; left: 0; width: 100%;
    text-align: center;
    font-family: "Playfair Display", serif;
    font-size: 15px; color: var(--muted); letter-spacing: .2px;
  }
  .kicker {
    position: absolute; top: 36px; left: 50%; transform: translateX(-50%);
    background: var(--pink);
    color: var(--white);
    font-weight: 700; font-size: 25px;
    padding: 3px 26px; border-radius: 22px;
  }
  .lead {
    position: absolute; top: 82px; left: 0; width: 100%;
    text-align: center;
    font-weight: 700; font-size: 42px; color: var(--ink);
    letter-spacing: 2px;
  }
  .accent-script {
    position: absolute; top: 196px; left: 86px;
    width: 196px; height: 84px;
    border: 3px solid var(--pink); border-radius: 50%;
    display: flex; align-items: center; justify-content: center;
    font-family: "Klee One", cursive;
    font-size: 32px; color: var(--pink);
    transform: rotate(-8deg);
    background: rgba(255,255,255,.6);
  }
  .title-main {
    position: absolute;
    font-weight: 900; color: var(--magenta);
    letter-spacing: 2px; line-height: 1;
    text-shadow: 0 0 6px #fff, 0 0 10px #fff;
  }
  .title-main.line-1 { top: 176px; left: 298px; font-size: 86px; }
  .title-main.line-2 { top: 274px; left: 0; width: 100%; text-align: center; font-size: 98px; }
  .title-sub {
    position: absolute; top: 384px; left: 0; width: 100%;
    text-align: center;
    font-weight: 900; font-size: 62px; color: var(--sky);
    letter-spacing: 3px; line-height: 1;
    text-shadow: 0 0 6px #fff;
  }
  .author {
    position: absolute; top: 456px; left: 0; width: 100%;
    display: flex; justify-content: center; align-items: baseline; gap: 18px;
    color: var(--ink);
  }
  .author .role { font-size: 15px; font-weight: 500; }
  .author .name { font-family: "Playfair Display", serif; font-size: 34px; }
  .photo { position: absolute; }
  .photo.portrait {
    left: 0; top: 500px; width: 262px; height: 475px;
    background: linear-gradient(180deg, #f4dfe6 0%, #b9cbe3 55%, #8fb1d6 100%);
  }
  .photo.pool {
    left: 262px; top: 500px; width: 489px; height: 345px;
    background: linear-gradient(160deg, #d7d4c6 0%, #88a47a 40%, #5fb6c9 70%, #a88d6e 100%);
  }
  .photo.laptop {
    left: 262px; top: 845px; width: 168px; height: 130px;
    background: linear-gradient(180deg, #e8e3e0 0%, #d9c9c8 100%);
  }
  .photo.group {
    left: 430px; top: 845px; width: 321px; height: 130px;
    background: linear-gradient(135deg, #c7b19a 0%, #a3b8c9 50%, #d6c6b8 100%);
  }
  .band {
    position: absolute; left: 0; top: 975px; width: 751px; height: 225px;
    background: linear-gradient(180deg, #f27bb0 0%, var(--pink-deep) 100%);
  }
  .pc-badge {
    position: absolute; left: 12px; top: 1010px;
    width: 84px; height: 84px; border-radius: 50%;
    background: var(--white);
    color: var(--pink-deep);
    font-weight: 900; font-size: 20px; line-height: 1.15;
    display: flex; flex-direction: column; align-items: center; justify-content: center;
  }
  .assets {
    position: absolute; left: 108px; top: 992px;
    display: flex; gap: 8px; align-items: center;
  }
  .asset {
    background: var(--white); color: var(--pink-deep);
    font-weight: 700; font-size: 21px; line-height: 1.4;
    padding: 0 12px; border-radius: 20px;
  }
  .zero { color: var(--white); font-weight: 900; font-size: 27px; margin-left: 6px; }
  .freedoms {
    position: absolute; left: 108px; top: 1046px;
    display: flex; gap: 10px; align-items: center;
  }
  .freedom {
    background: var(--white); color: var(--pink-deep);
    font-weight: 900; font-size: 30px;
    padding: 0 10px; border-radius: 10px; line-height: 1.35;
  }
  .freedom-join { color: var(--white); font-weight: 900; font-size: 30px; }
  .promise {
    position: absolute; left: 0; top: 1118px; width: 100%;
    text-align: center;
    color: var(--white); font-weight: 900; font-size: 38px; line-height: 1.3;
  }
</style>
</head>
<body>
<div class="cover">
  <p class="tagline-en">This life only once.I want to be more like myself and shine more.</p>
  <p class="kicker">きみの毎日は花になる!</p>
  <p class="lead">扉をそっと叩いて</p>

  <p class="accent-script">心ほどける</p>
  <h1>
    <span class="title-main line-1">日々を選び</span>
    <span class="title-main line-2">取るための</span>
    <span class="title-sub">小さな習慣集</span>
  </h1>

  <p class="author"><span class="role">スカイハーベスター</span><span class="name">Sora</span></p>

  <div class="photo portrait" role="img" aria-label="明るい部屋でノートパソコンを抱えて微笑む水色のワンピースの女性"></div>
  <div class="photo pool" role="img" aria-label="南国の庭のプールサイドでノートパソコンを開いて仕事をする女性"></div>
  <div class="photo laptop" role="img" aria-label="白いテーブルでパソコンに向かう女性"></div>
  <div class="photo group" role="img" aria-label="海外の学校で子どもたちと並ぶ集合写真"></div>

  <div class="band"></div>
  <div class="pc-badge"><span>PC</span><span>1台で</span></div>
  <div class="assets">
    <span class="asset">知識</span>
    <span class="asset">人脈</span>
    <span class="asset">実績</span>
    <span class="asset">経験</span>
    <span class="asset">貯金</span>
    <span class="zero">すべてゼロでも</span>
  </div>
  <div class="freedoms">
    <span class="freedom">好きな時に</span>
    <span class="freedom">好きな場所で</span>
    <span class="freedom">好きな人</span><span class="freedom-join">と</span>
  </div>
  <p class="promise">自分らしくグローバルに生きていく方法</p>
</div>
</body>
</html>
```